Campaign Flyer for a local election

Black and white election flyer

See information below to be included:

Re-elect Dorian
Experienced Willows Board Member
Experienced NYC Principal
Experienced leader

One Year Board Accomplishments:
-Installed New Park Lights (Bollards)
-Red Brick Road Repair Project
-Established Closer Ties with Our local precinct to frequently monitor the community with directed security patrols. Requested an increased police presence.
-Met with the 62nd Precinct Officials & Assemblywoman, Marla Quintrell to discuss our security issues
- Focused on maintenance of streetlights to make brighter streets
-Negotiated Contract & Hired Our New Landscaper, Oakhollow Landscapers
-Major Homeowner Shrub Replacement Project
- Addressing Standing Water in our Park (Installed French Drain)
- Replaced and upgraded all 5 outdoor circuit breaker panels
-Write monthly community newsletters
-Sewer cleaning project (had all community catch basins cleaned)
-Carefully overseeing our new school project. Coordinating with the sponsor and the school directors
-Delivered a very healthy budget to the community
-Works closely with our committees
-Events: Zoo event, Petting Zoo, Outdoor Movie Night, Egg Hunt

It is my intent to seek re-election.
(Photo) Dorian Lindqvist
-Dedicated to improving our community
-Hard-working…He gets thing done!
-Trustworthy

. .

Please note, I am submitting new information under accomplishments. The list of accomplishments should be in the same sequence, starting with: Met with the 62nd Precinct....
Please carefully review.
----------------------------------------------------------------------------------------------------------------------------------------------------------------

Re-elect Dorian
Experienced NYC Principal
Experienced leader

Last Year’s Board Accomplishments:

-Met with the 62nd Precinct Officials & Assemblywoman, Marla Quintrell, to discuss our security issues. Requested increased police presence.
-Established a strong partnership with the 62nd precinct to frequently monitor the community with directed security patrols.
-Replaced all new park lights (Bollards) to make the park brighter
- Focused on maintenance of streetlights to make streets brighter
-‘Fixing Our Streets Project’ (Repaired all cracked/missing red bricks)
-Homeowner Shrub Replacement Project (Replaced hundreds of bushes)
- I write the monthly community newsletter
-Carefully overseeing our new school project. Coordinating with the sponsor and the school director
-Monitoring C of O’s and homeowners Insurance

(Photo) Dorian Lindqvist
-Hard-working! I get things done!
-Trustworthy

. .

Re-elect Dorian
Experienced NYC Principal
Experienced leader

(Photo) Dorian Lindqvist
-Trustworthy

. .

Target Market(s)

A Community electing a Board Member

Industry/Entity Type

residential election

Requirements
Must have
• all black, white and grey print. Flyers will not be printed in color
Nice to have
• See the information in the attachment below containing all my accomplishments
Should not have
• color

```html
<!DOCTYPE html>
<html lang="en">
<head>
<meta charset="utf-8">
<title>Re-elect Dorian – Campaign Flyer</title>
<link href="https://fonts.googleapis.com/css2?family=Anton&family=Figtree:wght@400;700;800&display=swap" rel="stylesheet">
<style>
  :root{
    --ink:#0d0d0d;
    --paper:#ffffff;
    --backdrop:#b3b3b3;
    --silver-light:#d9d9d9;
    --silver-dark:#1a1a1a;
    --photo-light:#9a9a9a;
    --photo-dark:#3a3a3a;
    --rule:#8a8a8a;
  }
  *{margin:0;padding:0;box-sizing:border-box}
  html,body{width:970px;height:1200px;overflow:hidden;background:var(--backdrop)}
  .flyer{position:absolute;left:82px;top:77px;width:806px;height:1044px;background:var(--ink);overflow:hidden;box-shadow:0 14px 18px rgba(0,0,0,.25)}
  .flyer-shapes{position:absolute;inset:0}
  .headline{position:absolute;left:37px;top:22px;font-family:"Anton",sans-serif;font-size:116px;line-height:1;color:var(--paper);letter-spacing:-1px;white-space:nowrap}
  .credentials{position:absolute;left:40px;top:148px;list-style:none}
  .credentials li{display:flex;align-items:center;height:34px;font-family:"Anton",sans-serif;font-size:27px;color:var(--paper);letter-spacing:-.3px;white-space:nowrap}
  .credentials svg{width:22px;height:22px;margin-right:22px}
  .accomplishments{position:absolute;left:38px;top:344px;width:304px}
  .accomplishments h2{font-family:"Anton",sans-serif;font-weight:400;font-size:21.5px;color:var(--ink);letter-spacing:-.2px;line-height:1.3;white-space:nowrap;padding-bottom:2px;border-bottom:3px solid var(--ink)}
  .accomplishments ul{list-style:none;margin-top:9px}
  .accomplishments li{position:relative;padding-left:26px;font-family:"Figtree",sans-serif;font-size:14.3px;line-height:17.3px;color:var(--ink);margin-bottom:7px}
  .accomplishments li svg{position:absolute;left:1px;top:2px;width:14px;height:14px}
  .candidate{position:absolute;left:355px;width:451px;text-align:center;color:var(--paper)}
  .candidate-name{top:836px;font-family:"Anton",sans-serif;font-size:62px;line-height:1.1;letter-spacing:-.5px;white-space:nowrap}
  .intent{position:absolute;left:397px;top:913px;width:370px;height:33px;border-top:2px solid var(--rule);border-bottom:2px solid var(--rule);font-family:"Figtree",sans-serif;font-weight:800;font-size:19.5px;line-height:29px;text-align:center;color:var(--paper)}
  .qualities{position:absolute;left:355px;top:956px;width:451px;list-style:none;text-align:center}
  .qualities li{font-family:"Figtree",sans-serif;font-weight:700;font-size:15.5px;line-height:18.5px;color:var(--paper)}
  .qualities svg{width:11px;height:11px;margin-right:8px;vertical-align:-1px}
</style>
</head>
<body>
<div class="flyer">
  <svg class="flyer-shapes" viewBox="0 0 806 1044" width="806" height="1044">
    <defs>
      <linearGradient id="silverBand" x1="0" y1="0" x2="1" y2="0">
        <stop offset="0" stop-color="var(--silver-dark)"/>
        <stop offset=".45" stop-color="var(--silver-light)"/>
        <stop offset="1" stop-color="var(--silver-dark)"/>
      </linearGradient>
      <linearGradient id="photoTone" x1="0" y1="0" x2="0" y2="1">
        <stop offset="0" stop-color="var(--photo-light)"/>
        <stop offset="1" stop-color="var(--photo-dark)"/>
      </linearGradient>
    </defs>
    <polygon points="0,348 355,262 355,1044 0,1044" fill="var(--paper)"/>
    <polygon points="355,262 806,134 806,149 355,288" fill="url(#silverBand)"/>
    <polygon points="0,340 355,254 355,262 0,348" fill="url(#silverBand)" opacity=".5"/>
    <polygon points="355,288 806,149 806,703 355,815" fill="url(#photoTone)" role="img" aria-label="Portrait photo of the candidate smiling, wearing glasses, standing on beach dunes with sea behind"/>
    <polygon points="355,815 806,703 806,717 355,832" fill="url(#silverBand)"/>
  </svg>

  <h1 class="headline">Re - elect Dorian</h1>

  <ul class="credentials">
    <li><svg viewBox="0 0 22 22"><path d="M3 11.5l5 5L19 5" fill="none" stroke="#fff" stroke-width="3.4" stroke-linecap="round" stroke-linejoin="round"/></svg>EXPERIENCED WILLOWS BOARD MEMBER</li>
    <li><svg viewBox="0 0 22 22"><path d="M3 11.5l5 5L19 5" fill="none" stroke="#fff" stroke-width="3.4" stroke-linecap="round" stroke-linejoin="round"/></svg>EXPERIENCED NYC PRINCIPAL</li>
    <li><svg viewBox="0 0 22 22"><path d="M3 11.5l5 5L19 5" fill="none" stroke="#fff" stroke-width="3.4" stroke-linecap="round" stroke-linejoin="round"/></svg>EXPERIENCED LEADER</li>
  </ul>

  <section class="accomplishments">
    <h2>One Year Board ACCOMPLISHMENTS:</h2>
    <ul>
      <li><svg viewBox="0 0 14 14"><rect x="1" y="2" width="11" height="11" rx="2" fill="none" stroke="#0d0d0d" stroke-width="1.5"/><path d="M3.5 7.5l2.5 2.5L13 2" fill="none" stroke="#0d0d0d" stroke-width="2" stroke-linecap="round"/></svg>Installed New Park Lights (Bollards)</li>
      <li><svg viewBox="0 0 14 14"><rect x="1" y="2" width="11" height="11" rx="2" fill="none" stroke="#0d0d0d" stroke-width="1.5"/><path d="M3.5 7.5l2.5 2.5L13 2" fill="none" stroke="#0d0d0d" stroke-width="2" stroke-linecap="round"/></svg>Red Brick Road Repair Project</li>
      <li><svg viewBox="0 0 14 14"><rect x="1" y="2" width="11" height="11" rx="2" fill="none" stroke="#0d0d0d" stroke-width="1.5"/><path d="M3.5 7.5l2.5 2.5L13 2" fill="none" stroke="#0d0d0d" stroke-width="2" stroke-linecap="round"/></svg>Established Closer Ties with Our local precinct to frequently monitor the community with directed security patrols. Requested an increased police presence.</li>
      <li><svg viewBox="0 0 14 14"><rect x="1" y="2" width="11" height="11" rx="2" fill="none" stroke="#0d0d0d" stroke-width="1.5"/><path d="M3.5 7.5l2.5 2.5L13 2" fill="none" stroke="#0d0d0d" stroke-width="2" stroke-linecap="round"/></svg>Met with the 62nd Precinct Officials &amp; Assemblywoman, Marla Quintrell to discuss our security issues</li>
      <li><svg viewBox="0 0 14 14"><rect x="1" y="2" width="11" height="11" rx="2" fill="none" stroke="#0d0d0d" stroke-width="1.5"/><path d="M3.5 7.5l2.5 2.5L13 2" fill="none" stroke="#0d0d0d" stroke-width="2" stroke-linecap="round"/></svg>Focused on maintenance of streetlights to make brighter streets</li>
      <li><svg viewBox="0 0 14 14"><rect x="1" y="2" width="11" height="11" rx="2" fill="none" stroke="#0d0d0d" stroke-width="1.5"/><path d="M3.5 7.5l2.5 2.5L13 2" fill="none" stroke="#0d0d0d" stroke-width="2" stroke-linecap="round"/></svg>Negotiated Contract &amp; Hired Our New Landscaper, Oakhollow Landscapers</li>
      <li><svg viewBox="0 0 14 14"><rect x="1" y="2" width="11" height="11" rx="2" fill="none" stroke="#0d0d0d" stroke-width="1.5"/><path d="M3.5 7.5l2.5 2.5L13 2" fill="none" stroke="#0d0d0d" stroke-width="2" stroke-linecap="round"/></svg>Major Homeowner Shrub Replacement Project</li>
      <li><svg viewBox="0 0 14 14"><rect x="1" y="2" width="11" height="11" rx="2" fill="none" stroke="#0d0d0d" stroke-width="1.5"/><path d="M3.5 7.5l2.5 2.5L13 2" fill="none" stroke="#0d0d0d" stroke-width="2" stroke-linecap="round"/></svg>Addressing Standing Water in our Park (Installed French Drain)</li>
      <li><svg viewBox="0 0 14 14"><rect x="1" y="2" width="11" height="11" rx="2" fill="none" stroke="#0d0d0d" stroke-width="1.5"/><path d="M3.5 7.5l2.5 2.5L13 2" fill="none" stroke="#0d0d0d" stroke-width="2" stroke-linecap="round"/></svg>Replaced and upgraded all 5 outdoor circuit breaker panels</li>
      <li><svg viewBox="0 0 14 14"><rect x="1" y="2" width="11" height="11" rx="2" fill="none" stroke="#0d0d0d" stroke-width="1.5"/><path d="M3.5 7.5l2.5 2.5L13 2" fill="none" stroke="#0d0d0d" stroke-width="2" stroke-linecap="round"/></svg>Write monthly community newsletters</li>
      <li><svg viewBox="0 0 14 14"><rect x="1" y="2" width="11" height="11" rx="2" fill="none" stroke="#0d0d0d" stroke-width="1.5"/><path d="M3.5 7.5l2.5 2.5L13 2" fill="none" stroke="#0d0d0d" stroke-width="2" stroke-linecap="round"/></svg>Sewer cleaning project (had all community catch basins cleaned)</li>
      <li><svg viewBox="0 0 14 14"><rect x="1" y="2" width="11" height="11" rx="2" fill="none" stroke="#0d0d0d" stroke-width="1.5"/><path d="M3.5 7.5l2.5 2.5L13 2" fill="none" stroke="#0d0d0d" stroke-width="2" stroke-linecap="round"/></svg>Carefully overseeing our new school project. Coordinating with the sponsor and the school directors</li>
      <li><svg viewBox="0 0 14 14"><rect x="1" y="2" width="11" height="11" rx="2" fill="none" stroke="#0d0d0d" stroke-width="1.5"/><path d="M3.5 7.5l2.5 2.5L13 2" fill="none" stroke="#0d0d0d" stroke-width="2" stroke-linecap="round"/></svg>Delivered a very healthy budget to the community</li>
      <li><svg viewBox="0 0 14 14"><rect x="1" y="2" width="11" height="11" rx="2" fill="none" stroke="#0d0d0d" stroke-width="1.5"/><path d="M3.5 7.5l2.5 2.5L13 2" fill="none" stroke="#0d0d0d" stroke-width="2" stroke-linecap="round"/></svg>Works closely with our committees</li>
      <li><svg viewBox="0 0 14 14"><rect x="1" y="2" width="11" height="11" rx="2" fill="none" stroke="#0d0d0d" stroke-width="1.5"/><path d="M3.5 7.5l2.5 2.5L13 2" fill="none" stroke="#0d0d0d" stroke-width="2" stroke-linecap="round"/></svg>Events: Zoo event, Petting Zoo, Outdoor Movie Night, Egg Hunt</li>
    </ul>
  </section>

  <h2 class="candidate candidate-name">Dorian Lindqvist</h2>
  <p class="intent">It is my intent to seek re-election.</p>
  <ul class="qualities">
    <li><svg viewBox="0 0 11 11"><circle cx="5.5" cy="5.5" r="5.5" fill="#fff"/><path d="M4.3 3l2.5 2.5L4.3 8" fill="none" stroke="#0d0d0d" stroke-width="1.6"/></svg>Dedicated to improving our community</li>
    <li><svg viewBox="0 0 11 11"><circle cx="5.5" cy="5.5" r="5.5" fill="#fff"/><path d="M4.3 3l2.5 2.5L4.3 8" fill="none" stroke="#0d0d0d" stroke-width="1.6"/></svg>Hard-working…He gets thing done!</li>
    <li><svg viewBox="0 0 11 11"><circle cx="5.5" cy="5.5" r="5.5" fill="#fff"/><path d="M4.3 3l2.5 2.5L4.3 8" fill="none" stroke="#0d0d0d" stroke-width="1.6"/></svg>Trustworthy</li>
  </ul>
</div>
</body>
</html>
```